Paws Of Kindness Business cards

Design a cool, modern business card for my bully breed rescue.

Contact Information for Business Card

Marlene
517-382-4061 Marlene@PawsOfKindnessRescue.net PawsOfKindnessRescue.net

Font styles to use
Serif
Sans Serif

Colors

Designer to choose colors to be used in the design.

Requirements
Must have
• logo and info. Color
Nice to have
• Foil. Maybe some paw prints on the back or some kind of dog illustration.

```html
<!DOCTYPE html>
<html lang="en">
<head>
<meta charset="utf-8">
<title>Paws Of Kindness – Business Cards</title>
<link rel="stylesheet" href="https://fonts.googleapis.com/css2?family=Arimo:wght@400;700&display=swap">
<style>
  :root {
    --page: #ffffff;
    --card: #ffffff;
    --card-edge: #c9c9c9;
    --band-dark: #4f5052;
    --band-light: #7c7c7e;
    --ink: #111111;
    --ink-faint: #48494b;
    --ink-ghost: #d2d2d2;
  }
  html, body {
    margin: 0;
    padding: 0;
    width: 1200px;
    height: 1200px;
    overflow: hidden;
    background: var(--page);
  }
  .sheet {
    position: relative;
    width: 1200px;
    height: 1200px;
  }
  .card {
    position: absolute;
    left: 180px;
    width: 840px;
    height: 514px;
    display: block;
  }
  .card--front { top: 48px; }
  .card--back { top: 638px; }
  .card-text {
    font-family: "Arimo", Arial, sans-serif;
  }
  .brand-name { font-weight: 700; fill: var(--ink); }
  .brand-ghost { font-weight: 700; fill: var(--ink-faint); }
  .brand-mini { font-weight: 700; fill: var(--ink-ghost); }
  .contact { font-weight: 400; fill: var(--ink); font-size: 26px; }
</style>
</head>
<body>
<main class="sheet">

  <!-- Front of card -->
  <svg class="card card--front" viewBox="0 0 840 514" xmlns="http://www.w3.org/2000/svg" aria-label="Business card front">
    <defs>
      <linearGradient id="bandFront" x1="0" y1="1" x2="1" y2="0">
        <stop offset="0" stop-color="var(--band-dark)"/>
        <stop offset="0.55" stop-color="#5a5b5d"/>
        <stop offset="1" stop-color="var(--band-light)"/>
      </linearGradient>
    </defs>
    <rect class="card-base" x="0.5" y="0.5" width="839" height="513" fill="var(--card)" stroke="var(--card-edge)"/>
    <polygon class="card-band" points="0,138 840,0 840,374 0,514" fill="url(#bandFront)"/>

    <g class="brand-lockup">
      <circle cx="220" cy="70" r="40" fill="none" stroke="var(--ink)" stroke-width="3"/>
      <text class="card-text brand-name" x="220" y="166" font-size="44" text-anchor="middle">Paws Of Kindness</text>
    </g>

    <g class="contact-block card-text" text-anchor="middle">
      <text class="contact" x="602" y="336">Marlene</text>
      <text class="contact" x="602" y="381">517-382-4061</text>
      <text class="contact" x="602" y="427">Marlene@PawsOfKindnessRescue.net</text>
      <text class="contact" x="602" y="472">PawsOfKindnessRescue.net</text>
    </g>
  </svg>

  <!-- Back of card -->
  <svg class="card card--back" viewBox="0 0 840 514" xmlns="http://www.w3.org/2000/svg" aria-label="Business card back">
    <defs>
      <linearGradient id="bandBack" x1="0" y1="1" x2="1" y2="0">
        <stop offset="0" stop-color="var(--band-dark)"/>
        <stop offset="0.55" stop-color="#5a5b5d"/>
        <stop offset="1" stop-color="var(--band-light)"/>
      </linearGradient>
    </defs>
    <rect class="card-base" x="0.5" y="0.5" width="839" height="513" fill="var(--card)" stroke="var(--card-edge)"/>
    <polygon class="card-band" points="0,139 840,0 840,374 0,514" fill="url(#bandBack)"/>

    <g class="brand-mark-small">
      <circle cx="67" cy="44" r="8" fill="none" stroke="var(--ink-ghost)" stroke-width="1.5"/>
      <text class="card-text brand-mini" x="67" y="66" font-size="9" text-anchor="middle">Paws Of Kindness</text>
    </g>

    <g class="brand-mark-large">
      <circle cx="418" cy="186" r="40" fill="none" stroke="var(--ink-faint)" stroke-width="3"/>
      <text class="card-text brand-ghost" x="418" y="282" font-size="44" text-anchor="middle">Paws Of Kindness</text>
    </g>

    <g class="brand-mark-small">
      <circle cx="754" cy="448" r="8" fill="none" stroke="var(--ink-ghost)" stroke-width="1.5"/>
      <text class="card-text brand-mini" x="754" y="470" font-size="9" text-anchor="middle">Paws Of Kindness</text>
    </g>
  </svg>

</main>
</body>
</html>
```